An innovative landscaping company seeking a bold, creative stationary design.

I am a fast growing company specialising in quality plants and pots. Supplying corporate companies, designing landscapes for new builds, renovations of old gardens while caring for maintenance .

I need a Logo, business card (double sided) letterhead (for invoicing and client communications) compliment slips and an sign to place on site when working to advertise my company.

Design: I need a simple, clean, bold, Artistic design that is professional and mature. It should look good on a variety of mediums and be easy for printing. The design should make an impact to reflect I am innovative and different to others. I live in Africa so any image should represent a plant only.

Logo; Should be of a plant in a modern design ( could be a plant & pot or only plant)Colours should be green, black and white(refer to my attached)

I like the design of the attached file heaps. If something could be done like this I'd be happy!!!!

Target Market(s)

Corporarate companies and residential houses

Industry/Entity Type

Landscape Gardening

Font styles to use
Other font styles liked:
• Arial or open to suggestion

Colors
acd136
333333
fbfbfb
f37122

Requirements
Must have
• A logo that can follow through on all of my stationary, uniforms, signs etc. Nice if it was linear and artistic.
• My website has not been designed yet. This is something I hope to give to the winning designer. My website should be included though.
• Dara Okonbe
• Managing Director
• +234 8093172608
• www.tallfernyards.example
• dara@tallfernyards.example
• info@tallfernyards.example
• I currently have no shop and so don't want to include an address yet.
Nice to have
• A slogan.
• Create Cultivate Care
• If any designer has ideas I am open to suggestions for my logo.
Should not have
• Actual pictures of flowers or trees. Needs to be slightly abstract in linear form. Refer to attached business card image.

```html
<!DOCTYPE html>
<html lang="en">
<head>
<meta charset="utf-8">
<title>Tall Fern Yards — Stationery Set</title>
<link href="https://fonts.googleapis.com/css2?family=Questrial&display=swap" rel="stylesheet">
<style>
  :root {
    --leaf: #acd136;
    --ink: #333333;
    --paper: #fbfbfb;
    --white: #ffffff;
    --clay: #f37122;
    --stage: #ffffff;
    --backdrop: #e9ece4;
    --post: #5a5f56;
  }
  * { box-sizing: border-box; margin: 0; padding: 0; }
  html, body { width: 833px; height: 1200px; overflow: hidden; }
  body {
    position: relative;
    background: var(--stage);
    font-family: "Questrial", Arial, sans-serif;
    color: var(--ink);
  }
  .sheet {
    position: absolute;
    background: var(--white);
    box-shadow: 0 1px 4px rgba(0,0,0,.28);
    overflow: hidden;
  }
  .band { position: absolute; background: var(--leaf); }
  .tagline { position: absolute; color: var(--white); font-size: 13px; letter-spacing: .3px; white-space: nowrap; }
  .fineprint { position: absolute; color: var(--white); font-size: 6px; letter-spacing: .2px; white-space: nowrap; }

  .brand {
    position: absolute;
    display: flex; align-items: center; gap: 5px;
    font-size: 11px; color: var(--ink); text-transform: uppercase; letter-spacing: .6px;
    white-space: nowrap;
  }
  .brand-square { width: 12px; height: 12px; background: var(--clay); flex: none; }
  .brand--stacked {
    flex-direction: column; align-items: center; gap: 6px;
    white-space: normal; text-align: center; line-height: 1.25;
  }
  .brand--stacked .brand-square { width: 22px; height: 22px; }

  /* Letterhead */
  .letterhead { left: 28px; top: 42px; width: 472px; height: 575px; }
  .letterhead .band { left: 0; top: 0; width: 100%; height: 103px; }
  .letterhead .tagline { left: 16px; top: 62px; }
  .letterhead .fineprint { left: 16px; top: 84px; }
  .letterhead .brand { right: 12px; top: 78px; }

  /* Business card front */
  .card-front { left: 520px; top: 111px; width: 286px; height: 181px; }
  .card-front .band { left: 0; top: 0; width: 197px; height: 100%; }
  .card-name { position: absolute; left: 40px; top: 60px; color: var(--white); font-size: 25px; white-space: nowrap; }
  .card-role { position: absolute; left: 62px; top: 94px; color: var(--white); font-size: 8px; white-space: nowrap; }
  .card-front .brand { left: 205px; top: 62px; width: 73px; font-size: 11px; }

  /* Business card back */
  .card-back { left: 520px; top: 311px; width: 286px; height: 189px; }
  .card-back .band { left: 80px; top: 0; width: 206px; height: 100%; }
  .card-back .tagline { left: 122px; top: 42px; font-size: 12px; }
  .contact-list { position: absolute; left: 148px; top: 92px; list-style: none; color: var(--white); font-size: 7px; line-height: 14px; }
  .card-back .brand { left: 6px; top: 66px; width: 68px; font-size: 10px; }

  /* Compliment slip */
  .slip { left: 245px; top: 533px; width: 561px; height: 195px; }
  .slip .band { left: 0; top: 0; width: 385px; height: 100%; }
  .slip .tagline { left: 16px; top: 20px; }
  .slip-greeting { position: absolute; left: 16px; top: 158px; color: var(--white); font-size: 11px; }
  .slip .fineprint { left: 16px; top: 174px; }
  .slip .brand { left: 400px; top: 62px; width: 146px; font-size: 15px; }
  .slip .brand .brand-square { width: 30px; height: 30px; }

  /* Site sign */
  .sign-stage { position: absolute; left: 28px; top: 745px; width: 778px; height: 422px; background: var(--backdrop); }
  .site-sign { position: absolute; left: 239px; top: 66px; width: 300px; height: 250px; background: var(--white); box-shadow: 0 1px 4px rgba(0,0,0,.25); overflow: hidden; }
  .site-sign .band { left: 0; top: 0; width: 100%; height: 120px; }
  .site-sign .tagline { left: 20px; top: 22px; font-size: 16px; }
  .site-sign .brand { left: 20px; top: 70px; font-size: 13px; }
  .sign-panel { position: absolute; left: 0; top: 120px; width: 150px; height: 130px; background: var(--clay); }
  .sign-call { position: absolute; left: 166px; top: 140px; width: 124px; color: var(--ink); font-size: 15px; line-height: 19px; text-transform: uppercase; }
  .sign-web { position: absolute; left: 166px; top: 210px; font-size: 8px; color: var(--ink); white-space: nowrap; }
  .sign-post { position: absolute; top: 316px; width: 6px; height: 90px; background: var(--post); }
  .sign-post--left { left: 279px; }
  .sign-post--right { left: 493px; }
</style>
</head>
<body>

  <section class="sheet letterhead" aria-label="Letterhead">
    <div class="band"></div>
    <p class="tagline">Create Cultivate Care</p>
    <p class="fineprint">+234 8093172608 &nbsp;|&nbsp; dara@tallfernyards.example &nbsp;|&nbsp; www.tallfernyards.example</p>
    <div class="brand"><span class="brand-square"></span>Tall Fern Yards</div>
  </section>

  <section class="sheet card-front" aria-label="Business card front">
    <div class="band"></div>
    <p class="card-name">Dara Okonbe</p>
    <p class="card-role">Managing Director</p>
    <div class="brand brand--stacked"><span class="brand-square"></span>Tall Fern Yards</div>
  </section>

  <section class="sheet card-back" aria-label="Business card back">
    <div class="band"></div>
    <p class="tagline">Create Cultivate Care</p>
    <ul class="contact-list">
      <li>+234 8093172608</li>
      <li>dara@tallfernyards.example</li>
      <li>info@tallfernyards.example</li>
      <li>www.tallfernyards.example</li>
    </ul>
    <div class="brand brand--stacked"><span class="brand-square"></span>Tall Fern Yards</div>
  </section>

  <section class="sheet slip" aria-label="Compliment slip">
    <div class="band"></div>
    <p class="tagline">Create Cultivate Care</p>
    <p class="slip-greeting">With Compliments</p>
    <p class="fineprint">+234 8093172608 &nbsp;|&nbsp; dara@tallfernyards.example &nbsp;|&nbsp; www.tallfernyards.example</p>
    <div class="brand brand--stacked"><span class="brand-square"></span>Tall Fern Yards</div>
  </section>

  <section class="sign-stage" aria-label="Site sign">
    <div class="sign-post sign-post--left"></div>
    <div class="sign-post sign-post--right"></div>
    <div class="site-sign">
      <div class="band"></div>
      <p class="tagline">Create Cultivate Care</p>
      <div class="brand"><span class="brand-square"></span>Tall Fern Yards</div>
      <div class="sign-panel"></div>
      <p class="sign-call">Call us on +234 8093172608</p>
      <p class="sign-web">www.tallfernyards.example</p>
    </div>
  </section>

</body>
</html>
```